A5 double sided Restaurant menu design

We require a double sided A5 menu to be designed based on an example we will attach in a file(herrera y solis)
I have also attached a draft of what is required. The first side is a drinks menu, the second side is a food menu.
The quality of the finish needs to be as good as the attached example or please do not bother to submit if you do not have very similar fonts and background design

Industry/Entity Type

Restaurant

Colors
ec1f27
7f7f7f

Requirements
Must have
• our logo and very similar design to (herrera y solis) example attached
Nice to have
• instead of the colour yellow, we would like to see it in light grey and red

```html
<!DOCTYPE html>
<html lang="en">
<head>
<meta charset="utf-8">
<title>Side Street — The Menu</title>
<link rel="stylesheet" href="https://fonts.googleapis.com/css2?family=Oswald:wght@300;400;500;600;700&display=swap">
<style>
  :root {
    --red: #ec1f27;
    --grey: #7f7f7f;
    --ink: #1d1d1d;
    --paper: #ffffff;
    --wall: #ececec;
    --wall-light: #f7f7f7;
  }
  * { margin: 0; padding: 0; box-sizing: border-box; }
  html, body { width: 846px; height: 1200px; overflow: hidden; background: var(--paper); }
  body { font-family: "Oswald", sans-serif; color: var(--ink); }

  .menu { position: relative; width: 846px; height: 1200px; background: var(--paper); }
  .wall {
    position: absolute; left: 32px; top: 32px; width: 784px; height: 1144px;
    background:
      radial-gradient(ellipse at 30% 20%, var(--wall-light) 0%, transparent 55%),
      radial-gradient(ellipse at 75% 70%, #f3f3f3 0%, transparent 60%),
      linear-gradient(160deg, #f1f1f1 0%, var(--wall) 45%, #f4f4f4 100%);
  }

  .brand-seal {
    position: absolute; left: 120px; top: 34px; width: 192px; height: 192px;
    border-radius: 50%; background: var(--paper); border: 8px solid var(--grey);
    display: flex; align-items: center; justify-content: center;
  }
  .brand-name { font-weight: 700; font-size: 34px; color: var(--ink); letter-spacing: 0.5px; text-transform: uppercase; }

  .title-band { position: absolute; left: 304px; top: 164px; width: 360px; height: 24px; background: var(--grey); }
  .title-ribbon {
    position: absolute; left: 312px; top: 96px; width: 396px; height: 72px; background: var(--red);
    clip-path: polygon(0 0, 100% 0, 94% 50%, 100% 100%, 0 100%);
  }
  .title {
    position: absolute; left: 366px; top: 92px; font-weight: 700; font-style: italic;
    font-size: 58px; line-height: 76px; color: var(--ink); letter-spacing: -1px; transform: skewX(-6deg);
  }

  .section-label {
    position: absolute; height: 40px; background: var(--red); padding: 0 18px;
    clip-path: polygon(3% 0, 100% 0, 97% 100%, 0 100%);
    font-weight: 600; font-size: 31px; line-height: 40px; color: var(--ink); white-space: nowrap;
  }
  .section-note { position: absolute; font-weight: 300; font-style: italic; font-size: 18px; white-space: nowrap; color: var(--ink); }

  .dish { position: absolute; font-weight: 400; font-size: 15.5px; line-height: 23px; white-space: nowrap; color: var(--ink); letter-spacing: -0.2px; }
  .dish b { font-weight: 600; }
  .dish i { font-weight: 300; }

  .price-row { position: absolute; left: 63px; width: 450px; display: flex; justify-content: space-between; font-size: 15.5px; white-space: nowrap; }
  .price-row b { font-weight: 600; }
  .price { font-weight: 400; }

  .sketch { position: absolute; opacity: 0.5; }
</style>
</head>
<body>
<main class="menu">
  <div class="wall"></div>

  <div class="sketch" role="img" aria-label="Line sketch of a cheese wheel" style="left:344px;top:820px;width:104px;height:84px;background:radial-gradient(ellipse,#d6d6d6,transparent 70%);"></div>
  <div class="sketch" role="img" aria-label="Line sketch of a sliced pizza" style="left:560px;top:904px;width:240px;height:256px;background:radial-gradient(circle,#d2d2d2 0%,#e2e2e2 55%,transparent 72%);"></div>
  <div class="sketch" role="img" aria-label="Line sketch of vegetables, herbs and a knife and fork" style="left:384px;top:936px;width:160px;height:200px;background:radial-gradient(ellipse,#dcdcdc,transparent 70%);"></div>

  <div class="brand-seal"><span class="brand-name">Side Street</span></div>

  <div class="title-band"></div>
  <div class="title-ribbon"></div>
  <h1 class="title">THE MENU</h1>

  <div class="section-label" style="left:70px;top:246px;">PIZZA / $20</div>
  <p class="section-note" style="left:308px;top:260px;">(w/ tomato sauce base and mozzarella cheese)</p>

  <p class="dish" style="left:67px;top:302px;"><b>AMERICANA</b> Spicy Salami, Oregano</p>
  <p class="dish" style="left:67px;top:338px;"><b>MARGHERITA</b> Mozzarella Cheese, Oregano, Fresh Basil</p>
  <p class="dish" style="left:67px;top:373px;"><b>TROPICALE</b> Ham, Pineapple</p>
  <p class="dish" style="left:67px;top:409px;"><b>VEGETERIANA</b> Onion, Mushrooms, Capsicum, Olives,<br>Spinach, Oregano, Parmesan, Garlic</p>
  <p class="dish" style="left:67px;top:467px;"><b>CALABRESE</b> Onion, Spicy Salami, Capsicum, Anchovies,<br>Olives, Oregano</p>
  <p class="dish" style="left:67px;top:525px;"><b>CAPRICCIOSA</b> Ham, Mushrooms, Italian Sausage,<br>Oregano, Chilli Flakes</p>

  <p class="dish" style="left:472px;top:302px;"><b>GAMBERI</b> Fresh Prawns, Oregano, Parmesan, Chilli<br>Flakes, Garlic</p>
  <p class="dish" style="left:472px;top:360px;"><b>MEAT LOVERS</b> Ham, Spicy Salami, Bacon, Cabanossi,<br>Italian Sausage</p>
  <p class="dish" style="left:472px;top:418px;"><b>POLLO</b> Onion, Mushrooms, Chicken Breast, Oregano,<br>Parmesan, Garlic</p>
  <p class="dish" style="left:472px;top:476px;"><b>SUPREMA</b> Onion, Ham, Spicy Salami, Mushrooms,<br>Bacon, Cabanossi, Capsicum, Olives, Oregano, Garlic</p>
  <p class="dish" style="left:472px;top:534px;"><b>TRICOLORE</b> Cherry Tomatoes, Oregano, Parmesan,<br>Garlic, Chilli Flakes, Fresh Rocket, Shaved Parmesan</p>

  <div class="section-label" style="left:64px;top:596px;">PASTA / $18</div>
  <p class="section-note" style="left:260px;top:606px;">(w/ Spaghetti, Fettuccine or Penne - All pasta w/ parmesan &amp; fresh parsley)</p>

  <p class="dish" style="left:63px;top:650px;line-height:27px;"><b>ARRABIATTA</b> Rich Tomato Sauce, Garlic, Chilli- <i>Add<br>prawn or chicken $3</i></p>
  <p class="dish" style="left:63px;top:718px;"><b>LASAGNE</b> Lasagna Sheets, Bolognese Sauce, Mozzarella</p>
  <p class="dish" style="left:63px;top:757px;line-height:27px;"><b>BOLOGNESE</b> Rich Tomato Sauce, Minced Beef &amp; Pork,<br>Onion, Celery, Carrot</p>
  <p class="dish" style="left:63px;top:824px;"><b>CARBONARA</b> Bacon, Eggs, Fresh Cream</p>

  <p class="dish" style="left:475px;top:650px;line-height:27px;"><b>MAMMA MIA</b> Italian Sausage, Mushrooms, Fresh Cream<br>&amp; Chilli in Napoletana Sauce</p>
  <p class="dish" style="left:475px;top:718px;line-height:27px;"><b>PESTO</b> Fresh Cream, Pine Nuts, Garlic, Pepper, Basil- <i>Add<br>prawn or chicken $3</i></p>
  <p class="dish" style="left:475px;top:784px;"><b>BOSCAIOLA</b> Ham, Mushrooms, Onion, Fresh Cream</p>

  <div class="section-label" style="left:68px;top:864px;">SHARE PLATES</div>

  <p class="price-row" style="top:920px;"><b>SICILIAN MIXED OLIVES</b><span class="price">8</span></p>
  <p class="price-row" style="top:948px;"><span><b>POLPETTE</b> Meatballs w/ciabatta bread</span><span class="price">18</span></p>
  <p class="price-row" style="top:981px;"><b>GARLIC/HERB BREAD</b><span class="price">8</span></p>
  <p class="price-row" style="top:1012px;"><span><b>ANTIPASTO</b> Selection of cured meats and cheeses (2 or 4)</span><span class="price">18/32</span></p>

  <div class="section-label" style="left:64px;top:1054px;">PASTA / $18</div>

  <p class="dish" style="left:63px;top:1104px;"><b>TIRAMISU</b></p>
  <p class="dish" style="left:246px;top:1104px;">12</p>
  <p class="dish" style="left:344px;top:1104px;"><b>CHOCONUT CALZONE (M)</b></p>
  <p class="dish" style="left:524px;top:1104px;">18</p>
</main>
</body>
</html>
```